How likely are people to engage in social distancing? We need a good illustration to show the data!

We surveyed U.S. adults March 20th - 24th, 2020 and asked how likely they were to engage in social distancing (and other COVID-19 related health behaviors). What did the survey find? Basically, most people intend to engage in social distancing behaviors (e.g., avoiding large crowds) and other behaviors that reduce the spread of COVID-19 (e.g., washing hands at least 20 seconds). When most people intend to engage in a behavior, then public health professionals try to leverage that to move more people to act.
Now we need innovative and professional images that attempt to communicate one or all of these findings. The specific findings are nicely summarized in the attached document. For example, 82% of participants intend to engage in social distancing.
What sort of visual are we looking for? Our preference is for an original illustration (or set of illustrations). Our preference is for (creative and powerful illustrations, but we are also open to the creative and well-executed infographics.
We need these images fast . We will award monetary prizes to the 3 best designs. If we like more than that, then we might purchase more (e.g., in past contests, we have purchased as many as 30 designs).
What we will need:
(1) The illustrations must be original and we will need the photoshop and/or illustrator files for all artwork.
(2) You can illustrate all of the findings or just one of them. We need creative approaches that do a lucid job of bringing the data to life. Most people intend to engage in these behaviors. How to communicate that? Corvantists and Halmerites do not differ in their intentions; how to communicate that?
(3) The illustration should say, somewhere: "Based on a survey of 400 U.S. adults conducted March 20 - 24th, 2020."

U.S. Adults

• Original illustrations based on the findings of the survey (see attached document).

```html
<!DOCTYPE html>
<html lang="en">
<head>
<meta charset="utf-8">
<title>Survey of U.S. Adults</title>
<link rel="stylesheet" href="https://fonts.googleapis.com/css2?family=Anton&family=Montserrat:wght@400;600&family=Oswald:wght@600&display=swap">
<style>
:root{
  --bg:#8f8d8f;
  --paper:#ffffff;
  --section:#ececee;
  --panel:#e2e3e6;
  --red:#b81c2e;
  --navy:#1d4f91;
  --blue:#2aa3dc;
  --green:#7bbb3a;
  --orange:#f04e23;
  --yellow:#f5a623;
  --crimson:#c3202f;
  --teal:#2a9a8c;
  --ink:#3a3a3c;
  --muted:#6d6e71;
  --pink:#e8a3b0;
  --pink-soft:#f2c9d1;
  --sky:#a9d4ea;
  --sky-soft:#cfe6f3;
  --label:#d9dadd;
  --question:#a7a9ae;
}
*{box-sizing:border-box;margin:0;padding:0}
html,body{width:1200px;height:884px;overflow:hidden}
body{background:var(--bg);font-family:"Montserrat",sans-serif;color:var(--ink)}
.poster{position:absolute;left:300px;top:0;width:600px;height:884px;background:var(--paper);overflow:hidden}
.abs{position:absolute}

.header-band{left:210px;top:8px;width:360px;height:26px;background:var(--red)}
.title{left:150px;top:40px;width:440px;font-family:"Anton",sans-serif;font-weight:400;font-size:34px;color:var(--red);letter-spacing:1px;text-align:right;line-height:1}
.dates{left:150px;top:80px;width:440px;text-align:right;font-size:17px;line-height:1.2}
.tagline{left:150px;top:104px;width:440px;text-align:right;font-size:10px;color:var(--muted)}
.virus{border-radius:50%;background:radial-gradient(circle,var(--teal) 45%,#7cc6bc 100%)}
.virus.large{left:40px;top:100px;width:70px;height:70px}
.virus.small{left:100px;top:60px;width:38px;height:38px}
.map{left:200px;top:122px;width:180px;height:66px;border-radius:12px 30px 20px 40px;background:linear-gradient(#e3e4e6,#d3d4d7)}

.hub{left:0;top:0}
.hub text{font-family:"Montserrat",sans-serif;font-weight:600;font-size:14px;text-anchor:middle}
.hub-label{left:225px;top:272px;width:150px;text-align:center;font-family:"Anton",sans-serif;font-weight:400;font-size:22px;line-height:1.15;color:#2b2b2d}

.compare{left:0;top:515px;width:600px;height:369px;background:var(--section)}
.side-panel{left:480px;top:545px;width:100px;height:290px;background:var(--panel)}
.compare-title{left:140px;top:533px;width:320px;height:58px;border:2px solid #9a9b9e;text-align:center;font-family:"Anton",sans-serif;font-weight:400;font-size:21px;line-height:1.2;padding-top:3px;color:#3c3c3e}
.compare-title .red{color:var(--red)}
.compare-title .blue{color:var(--navy)}
.col-head{top:597px;font-family:"Oswald",sans-serif;font-size:16px;font-variant:small-caps;line-height:1.2}
.col-head.left{left:180px;color:var(--red)}
.col-head.right{left:360px;color:var(--navy)}

.row{position:absolute;left:0;width:600px;height:32px}
.row .label{position:absolute;left:18px;top:0;width:150px;height:32px;background:var(--label);font-size:9.5px;font-variant:small-caps;letter-spacing:.3px;line-height:1.1;padding:4px 8px;display:flex;align-items:center;color:#4a4a4c}
.row .bar{position:absolute;top:0;height:32px;display:flex;align-items:center;justify-content:center;font-family:"Oswald",sans-serif;font-size:14px}
.row .bar.c{left:178px;width:110px;background:linear-gradient(90deg,var(--pink) 70%,var(--pink-soft) 70%);color:var(--red)}
.row .bar.h{left:338px;width:130px;background:linear-gradient(90deg,var(--sky) 72%,var(--sky-soft) 72%);color:var(--navy)}
.row .icon{position:absolute;left:299px;top:2px;width:28px;height:28px;border-radius:50%;border:2px solid #7b7c7f;background:radial-gradient(circle,#cfd0d2 40%,#fff 42%)}
.spine{left:312px;top:615px;width:2px;height:226px;background:#9a9b9e}

.question{left:300px;top:846px;width:300px;height:38px;background:var(--question);color:#fff;font-size:9px;line-height:1.3;padding:5px 14px;text-align:center}
</style>
</head>
<body>
<main class="poster">
  <header>
    <div class="abs header-band"></div>
    <h1 class="abs title">SURVEY OF U.S. ADULTS</h1>
    <p class="abs dates">Conducted March 20th - 24th, 2020</p>
    <p class="abs tagline">Percent of Americans intending to engage in social distancing</p>
    <div class="abs virus large" role="img" aria-label="Teal virus particle illustration"></div>
    <div class="abs virus small" role="img" aria-label="Small teal virus particle illustration"></div>
    <div class="abs map" role="img" aria-label="Light grey map of the United States"></div>
  </header>

  <section class="abs hub" aria-label="Survey results">
    <svg width="600" height="515" viewBox="0 0 600 515">
      <g fill="none" stroke-width="3">
        <path d="M255.5 177.8 A130 130 0 0 1 383.6 200.4" stroke="var(--yellow)"/>
        <path d="M383.6 200.4 A130 130 0 0 1 429.5 288.7" stroke="var(--navy)"/>
        <path d="M429.5 288.7 A130 130 0 0 1 399.6 383.6" stroke="var(--crimson)"/>
        <path d="M399.6 383.6 A130 130 0 0 1 288.7 429.5" stroke="var(--orange)"/>
        <path d="M288.7 429.5 A130 130 0 0 1 200.4 383.6" stroke="var(--green)"/>
        <path d="M200.4 383.6 A130 130 0 0 1 174.4 266.4" stroke="var(--blue)"/>
      </g>
      <circle cx="300" cy="300" r="82" fill="#f1f2f4"/>
      <circle cx="300" cy="300" r="74" fill="#fff" stroke="#e0e1e4" stroke-width="2"/>
      <g stroke-width="11" fill="#fff">
        <circle cx="470" cy="190" r="44" stroke="var(--yellow)"/>
        <circle cx="495" cy="295" r="44" stroke="var(--navy)"/>
        <circle cx="465" cy="400" r="44" stroke="var(--crimson)"/>
        <circle cx="320" cy="450" r="44" stroke="var(--orange)"/>
        <circle cx="180" cy="425" r="44" stroke="var(--green)"/>
        <circle cx="140" cy="315" r="44" stroke="var(--blue)"/>
      </g>
      <circle cx="470" cy="200" r="22" fill="#e7c3a4" role="img" aria-label="Illustration of a hand declining a handshake"/>
      <circle cx="495" cy="305" r="22" fill="#c9d6ea" role="img" aria-label="Illustration of a hand sanitizer bottle"/>
      <circle cx="465" cy="410" r="22" fill="#e9c9cc" role="img" aria-label="Illustration of a crossed-out crowd"/>
      <circle cx="320" cy="460" r="22" fill="#f6cbb8" role="img" aria-label="Illustration of hands being washed for 20 seconds"/>
      <circle cx="180" cy="435" r="22" fill="#d7e8c4" role="img" aria-label="Illustration of two people standing apart"/>
      <circle cx="140" cy="325" r="22" fill="#cfe3f1" role="img" aria-label="Illustration of a person working from home"/>
      <circle cx="383.6" cy="200.4" r="4" fill="var(--yellow)"/>
      <circle cx="429.5" cy="288.7" r="4" fill="var(--navy)"/>
      <circle cx="399.6" cy="383.6" r="4" fill="var(--crimson)"/>
      <circle cx="288.7" cy="429.5" r="4" fill="var(--orange)"/>
      <circle cx="200.4" cy="383.6" r="4" fill="var(--green)"/>
      <text x="470" y="176" fill="var(--yellow)">85%</text>
      <text x="495" y="281" fill="var(--navy)">85%</text>
      <text x="465" y="386" fill="var(--crimson)">85%</text>
      <text x="320" y="436" fill="var(--orange)">87%</text>
      <text x="180" y="411" fill="var(--green)">82%</text>
      <text x="140" y="301" fill="var(--blue)">63%</text>
    </svg>
  </section>
  <p class="abs hub-label">SURVEY OF U.S.<br>ADULTS</p>

  <section class="abs compare" aria-label="Comparing Corvantists and Halmerites"></section>
  <div class="abs side-panel"></div>
  <h2 class="abs compare-title">COMPARING <span class="red">CORVANTISTS</span><br>AND <span class="blue">HALMERITES</span></h2>
  <span class="abs col-head left">Corvantist</span>
  <span class="abs col-head right">Halmerite</span>
  <div class="abs spine"></div>

  <div class="row" style="top:621px"><span class="label">Work from home</span><span class="bar c">60%</span><span class="icon" role="img" aria-label="Work from home icon"></span><span class="bar h">65%</span></div>
  <div class="row" style="top:659px"><span class="label">Engage in social distancing</span><span class="bar c">82%</span><span class="icon" role="img" aria-label="Social distancing icon"></span><span class="bar h">81%</span></div>
  <div class="row" style="top:697px"><span class="label">Avoid large gatherings</span><span class="bar c">60%</span><span class="icon" role="img" aria-label="No crowds icon"></span><span class="bar h">65%</span></div>
  <div class="row" style="top:735px"><span class="label">Put distance between yourself and other people</span><span class="bar c">85%</span><span class="icon" role="img" aria-label="No handshake icon"></span><span class="bar h">84%</span></div>
  <div class="row" style="top:773px"><span class="label">Wash hands at least 20 seconds</span><span class="bar c">87%</span><span class="icon" role="img" aria-label="Hand washing icon"></span><span class="bar h">88%</span></div>
  <div class="row" style="top:811px"><span class="label">Use hand sanitizer</span><span class="bar c">80%</span><span class="icon" role="img" aria-label="Hand sanitizer icon"></span><span class="bar h">82%</span></div>

  <p class="abs question">We would like to know how likely it is that you will perform these behaviors to slow the spread of coronavirus?</p>
</main>
</body>
</html>
```